Independence Day Graphics for Sale

I want to create 10 social media graphics (new Pixtaloo size 4:5 (1080 x 1350 pixels) focusing on our July 4th Sale Graphics, using any of the pics attached. Use the attached pics, NO RANDOM STOCK PHOTOGRAPHY. For the color scheme of the graphics, they should all be complementary to the product colors in the photos.
You can add any of the photos attached but none are required. You can do some of the graphics in all text. I mainly need BOLD text that says one of the headlines (10 total) SEE ATTACHED WORD DOCUMENT for the headlines to use.

Target Market(s)

women looking to lose weight

Requirements
Must have
• pics attached and text attached

```html
<!DOCTYPE html>
<html lang="en">
<head>
<meta charset="utf-8">
<title>Independence Day Sale Graphics</title>
<link rel="stylesheet" href="https://fonts.googleapis.com/css2?family=Montserrat:wght@800&family=Oswald:wght@600;700&display=swap">
<style>
  :root {
    --board: #a9a9a9;
    --white: #ffffff;
    --ink: #111111;
    --plum: #7b3a5e;
    --plum-light: #a4487f;
    --royal: #3d4db7;
    --indigo: #3d3a8a;
    --red: #dd2a27;
    --red-dark: #9e2c2c;
    --forest: #2e3b35;
    --sage-dark: #3f665e;
    --teal: #4e8a7f;
    --teal-light: #5d978b;
    --navy: #1f3a80;
    --mauve: #8c4079;
    --photo-light: #eeeef0;
    --photo-mid: #d9d9dd;
  }
  * { box-sizing: border-box; margin: 0; padding: 0; }
  html, body { width: 1200px; height: 3210px; overflow: hidden; }
  body { background: var(--board); position: relative; font-family: "Oswald", "Arial Narrow", sans-serif; }

  .tile { position: absolute; width: 460px; height: 574px; overflow: hidden; }
  .col-left { left: 116px; }
  .col-right { left: 609px; }
  .row-1 { top: 76px; } .row-2 { top: 694px; } .row-3 { top: 1312px; }
  .row-4 { top: 1923px; } .row-5 { top: 2541px; }

  .tile-bg { position: absolute; inset: 0; width: 100%; height: 100%; }

  .badge { position: absolute; display: flex; align-items: center; justify-content: center;
    font-family: "Montserrat", "Arial Black", sans-serif; font-weight: 800; color: var(--white);
    border-radius: 14px; transform: rotate(-2deg) skewX(-6deg); letter-spacing: 0.5px; white-space: nowrap; }
  .badge span { transform: skewX(6deg); }
  .badge sup { font-size: 0.55em; vertical-align: 0.7em; }
  .badge-outline { position: absolute; border: 1.5px solid; border-radius: 16px; transform: rotate(-2deg) skewX(-6deg); }

  .headline { position: absolute; left: 0; right: 0; text-align: center; font-weight: 700;
    text-transform: uppercase; line-height: 1.0; letter-spacing: -0.5px; }
  .headline.dark { color: var(--ink); }
  .headline.light { color: var(--white); }

  .photo { position: absolute; background: linear-gradient(180deg, var(--photo-light), var(--photo-mid)); border-radius: 6px; }

  .frame { position: absolute; inset: 35px; border: 3px solid var(--white); }
</style>
</head>
<body>

<!-- Tile 1 -->
<section class="tile col-left row-1">
  <svg class="tile-bg" viewBox="0 0 460 574" preserveAspectRatio="none" aria-hidden="true">
    <rect width="460" height="574" fill="var(--plum)"/>
    <path d="M0 0H460V229Q230 490 0 229Z" fill="var(--white)"/>
  </svg>
  <div class="badge-outline" style="left:96px;top:30px;width:290px;height:140px;border-color:var(--plum);"></div>
  <div class="badge" style="left:71px;top:17px;width:284px;height:76px;background:var(--plum);font-size:34px;"><span>JULY 4<sup>TH</sup></span></div>
  <div class="badge" style="left:108px;top:90px;width:277px;height:68px;background:var(--plum-light);font-size:33px;"><span>MEGA SALE!</span></div>
  <h2 class="headline dark" style="top:174px;font-size:68px;">25% OFF<br>EVERYTHING</h2>
  <div class="photo" role="img" aria-label="Row of four supplement bottles" style="left:30px;top:380px;width:400px;height:194px;"></div>
</section>

<!-- Tile 2 -->
<section class="tile col-right row-1">
  <svg class="tile-bg" viewBox="0 0 460 574" preserveAspectRatio="none" aria-hidden="true">
    <rect width="460" height="574" fill="var(--royal)"/>
    <path d="M0 0H460V229Q230 490 0 229Z" fill="var(--white)"/>
  </svg>
  <div class="badge-outline" style="left:100px;top:30px;width:318px;height:140px;border-color:var(--indigo);"></div>
  <div class="badge" style="left:74px;top:24px;width:287px;height:68px;background:var(--indigo);font-size:27px;"><span>BIGGEST 4<sup>TH</sup> OF</span></div>
  <div class="badge" style="left:110px;top:95px;width:300px;height:66px;background:var(--royal);font-size:26px;"><span>JULY SALE EVER!</span></div>
  <h2 class="headline dark" style="top:186px;font-size:68px;">25% OFF<br>SITEWIDE</h2>
  <div class="photo" role="img" aria-label="Group of four supplement bottles" style="left:70px;top:355px;width:380px;height:219px;"></div>
</section>

<!-- Tile 3 -->
<section class="tile col-left row-2">
  <svg class="tile-bg" viewBox="0 0 460 574" preserveAspectRatio="none" aria-hidden="true">
    <rect width="460" height="574" fill="var(--red)"/>
    <path d="M0 0H460V184Q230 434 0 184Z" fill="var(--white)"/>
  </svg>
  <div class="badge-outline" style="left:96px;top:60px;width:300px;height:158px;border-color:var(--red-dark);"></div>
  <div class="badge" style="left:62px;top:60px;width:312px;height:75px;background:var(--red-dark);font-size:30px;"><span>MEGA SUMMER</span></div>
  <div class="badge" style="left:103px;top:137px;width:292px;height:69px;background:var(--red);font-size:28px;"><span>BLOWOUT!</span></div>
  <h2 class="headline light" style="top:358px;font-size:82px;">25% OFF OF<br>EVERYTHING</h2>
</section>

<!-- Tile 4 -->
<section class="tile col-right row-2">
  <svg class="tile-bg" viewBox="0 0 460 574" preserveAspectRatio="none" aria-hidden="true">
    <rect width="460" height="574" fill="var(--sage-dark)"/>
    <path d="M0 0H460V184Q230 434 0 184Z" fill="var(--white)"/>
  </svg>
  <div class="badge-outline" style="left:80px;top:58px;width:330px;height:165px;border-color:var(--forest);"></div>
  <div class="badge" style="left:42px;top:48px;width:330px;height:84px;background:var(--forest);font-size:44px;"><span>ONE-TIME</span></div>
  <div class="badge" style="left:90px;top:131px;width:322px;height:80px;background:var(--sage-dark);font-size:44px;"><span>ONLY</span></div>
  <h2 class="headline light" style="top:358px;font-size:82px;">25% OFF OF<br>EVERYTHING !</h2>
</section>

<!-- Tile 5 -->
<section class="tile col-left row-3">
  <svg class="tile-bg" viewBox="0 0 460 574" preserveAspectRatio="none" aria-hidden="true">
    <rect width="460" height="574" fill="var(--plum)"/>
    <path d="M0 0H460V229Q230 490 0 229Z" fill="var(--white)"/>
  </svg>
  <div class="badge-outline" style="left:96px;top:30px;width:290px;height:140px;border-color:var(--plum);"></div>
  <div class="badge" style="left:71px;top:18px;width:284px;height:76px;background:var(--plum);font-size:34px;"><span>25% OFF</span></div>
  <div class="badge" style="left:108px;top:90px;width:277px;height:68px;background:var(--plum-light);font-size:25px;"><span>STOCK-UP EVENT</span></div>
  <h2 class="headline dark" style="top:186px;font-size:58px;">25% OFF ALL<br>SUPPLEMENTS</h2>
  <div class="photo" role="img" aria-label="Row of four supplement bottles" style="left:30px;top:380px;width:400px;height:194px;"></div>
</section>

<!-- Tile 6 -->
<section class="tile col-right row-3" style="background:radial-gradient(ellipse at 50% 45%, var(--teal-light), var(--teal));">
  <div class="headline light" style="top:82px;">
    <div style="font-size:56px;">THE LOWEST PRICES</div>
    <div style="font-size:100px;">WE'VE EVER</div>
    <div style="font-size:118px;">OFFERED!</div>
    <div style="font-size:118px;">25% OFF</div>
  </div>
</section>

<!-- Tile 7 -->
<section class="tile col-left row-4" style="background:linear-gradient(180deg, var(--photo-light) 0%, var(--photo-mid) 30%, var(--plum-light) 48%, var(--mauve) 100%);">
  <div class="photo" role="img" aria-label="Row of four supplement bottles" style="left:20px;top:0;width:420px;height:196px;background:transparent;"></div>
  <div class="headline light" style="top:212px;">
    <div style="font-size:52px;">THE LOWEST PRICES</div>
    <div style="font-size:92px;">WE'VE EVER</div>
    <div style="font-size:108px;">OFFERED!</div>
    <div style="font-size:108px;">25% OFF</div>
  </div>
</section>

<!-- Tile 8 -->
<section class="tile col-right row-4">
  <svg class="tile-bg" viewBox="0 0 460 574" preserveAspectRatio="none" aria-hidden="true">
    <rect width="460" height="574" fill="var(--red)"/>
    <path d="M0 0H460V170Q230 430 0 170Z" fill="var(--white)"/>
  </svg>
  <div class="badge-outline" style="left:96px;top:75px;width:300px;height:140px;border-color:var(--red-dark);"></div>
  <div class="badge" style="left:62px;top:60px;width:300px;height:72px;background:var(--red-dark);font-size:29px;"><span>HISTORIC 4<sup>TH</sup></span></div>
  <div class="badge" style="left:105px;top:138px;width:290px;height:68px;background:var(--red);font-size:27px;"><span>OF JULY SALE!</span></div>
  <h2 class="headline light" style="top:358px;font-size:82px;">25% OFF OF<br>EVERYTHING</h2>
</section>

<!-- Tile 9 -->
<section class="tile col-left row-5" style="background:var(--navy);">
  <div class="frame"></div>
  <div class="headline light" style="top:58px;">
    <div style="font-size:74px;">DON'T WAIT!</div>
    <div style="font-size:92px;">25% OFF</div>
    <div style="font-size:78px;">ENDS SOON</div>
  </div>
  <div class="photo" role="img" aria-label="Group of four supplement bottles" style="left:62px;top:325px;width:336px;height:205px;"></div>
</section>

<!-- Tile 10 -->
<section class="tile col-right row-5" style="background:var(--teal);">
  <div class="frame"></div>
  <div class="headline light" style="top:95px;">
    <div style="font-size:66px;">LAST CHANCE</div>
    <div style="font-size:100px;">25% OFF</div>
    <div style="font-size:108px;">TIME IS</div>
    <div style="font-size:62px;">RUNNING OUT!</div>
  </div>
</section>

</body>
</html>
```